KORVAL Works Pty Ltd. Website and Domain

www.korvalworks.com.au

require email addresses setup.

Info@korvalworks.com.au
accounts@korvalworks.com.au
peter.gralow@korvalworks.com.au
lucas.brenner@korvalworks.com.au

Website should promote commercial and domestic electrical services, audio visual services and data and fibre installations.

similar to my mates site www.bryfield.com.au

Website needs to promote professionalism, electrical/electrician, audio visual and data/fibre cabling installations.

promote environmental friendly imaginary.

Coding

Coded - Design and coding required

```html
<!DOCTYPE html>
<html lang="en">
<head>
<meta charset="utf-8">
<title>KORVAL Works Pty Ltd.</title>
<link href="https://fonts.googleapis.com/css2?family=IBM+Plex+Sans:wght@400;500;600;700&family=Source+Sans+3:wght@400;600&display=swap" rel="stylesheet">
<style>
:root{
  --blue:#1e88c9;
  --blue-dark:#1670a8;
  --green:#8cc63f;
  --ink:#222;
  --text:#333;
  --muted:#555;
  --footer:#222222;
  --white:#fff;
  --head:'IBM Plex Sans',sans-serif;
  --body:'Source Sans 3',sans-serif;
}
*{box-sizing:border-box;margin:0;padding:0}
html,body{width:1200px;height:3157px;overflow:hidden;background:var(--white)}
body{position:relative;font-family:var(--body);color:var(--text)}
.abs{position:absolute}
.brand{display:flex;align-items:center;gap:12px;color:var(--blue);font-family:var(--head);font-weight:600;font-size:26px;letter-spacing:.5px}
.brand-dot{width:62px;height:62px;border-radius:50%;background:var(--blue);flex:none}
/* header */
.site-header{left:0;top:0;width:1200px;height:116px}
.follow{left:688px;top:32px;font:500 10px var(--head);color:var(--ink);display:flex;align-items:center;gap:10px}
.social-dot{width:26px;height:26px;border-radius:50%;background:var(--blue)}
.callus{left:888px;top:24px;display:flex;gap:10px;align-items:center}
.callus small{display:block;font:500 10px var(--head);color:var(--ink)}
.callus strong{display:block;font:500 24px var(--head);color:var(--blue);line-height:1}
.nav{left:505px;top:75px;display:flex;gap:0;font:500 14px var(--head);color:var(--ink)}
.nav span{padding:4px 7px;margin-right:16px}
.nav .active{background:var(--blue);color:var(--white)}
/* hero */
.hero{left:0;top:116px;width:1200px;height:551px;background:linear-gradient(180deg,#5b5f9c 0%,#8b7fae 30%,#6b5a4a 55%,#3f4a3a 72%,#3a6a8f 100%)}
.hero h1{left:126px;top:96px;font:700 54px/56px var(--head);color:var(--white);letter-spacing:1px}
.hero p{left:129px;top:278px;font:400 28px/32px var(--head);color:var(--white)}
.btn-green{background:var(--green);color:var(--white);font-family:var(--head);font-weight:600;display:flex;align-items:center;justify-content:center}
.hero .btn-green{left:135px;top:371px;width:130px;height:44px;font-size:16px}
.dots{left:560px;top:504px;display:flex;gap:10px;align-items:center}
.dots i{width:7px;height:7px;border-radius:50%;background:var(--white);display:block}
.dots i.on{width:12px;height:12px;background:none;border:2px solid var(--white)}
/* headings */
.sec-title{font:700 26px var(--head);color:var(--blue);text-align:center;width:1200px;left:0}
.sec-rule{width:40px;height:3px;background:var(--blue);left:580px}
/* services */
.card{width:291px;text-align:center}
.card .photo{height:264px}
.card .badge{position:absolute;left:113px;top:222px;width:66px;height:66px;border-radius:50%;background:var(--white);display:flex;align-items:center;justify-content:center}
.card h3{font:600 14px var(--head);color:var(--ink);margin-top:30px}
.card p{font-size:13.5px;line-height:16px;color:var(--text);margin:18px 26px 0}
.card .btn-green{width:82px;height:27px;font-size:10px;margin:26px auto 0}
/* welcome */
.welcome{left:0;top:1287px;width:1200px;height:500px;background:#f3f0f1}
.welcome .photo{left:0;top:0;width:700px;height:500px;background:linear-gradient(90deg,#8d97a3 0%,#b7bec6 55%,#f3f0f1 100%)}
.welcome h2{left:701px;top:48px;font:600 28px var(--head);color:var(--blue)}
.welcome h2 span{display:block;font-size:50px;line-height:54px;font-weight:600}
.welcome .rule{left:701px;top:137px;width:84px;height:4px;background:var(--blue)}
.welcome p{left:701px;top:176px;width:378px;font-size:15.5px;line-height:20px;color:var(--text)}
.welcome .btn-green{left:706px;top:407px;width:120px;height:40px;font-size:16px}
/* why */
.why{left:0;top:1787px;width:1200px;height:513px;background:var(--blue);color:var(--white)}
.why .sec-title{color:var(--white);top:44px}
.why .sec-rule{background:var(--white);top:90px}
.feat{width:205px}
.feat h4{font:600 14px/20px var(--head)}
.feat p{font-size:13px;line-height:16px;margin-top:2px;color:#e8f3fb}
.feat-icon{width:80px;height:80px;border-radius:50%;background:var(--white);display:flex;align-items:center;justify-content:center}
.why .divider{height:1px;background:rgba(255,255,255,.35)}
.emblem{left:430px;top:140px;width:340px;height:320px;border-radius:50%;background:radial-gradient(circle,rgba(140,198,63,.35) 0%,rgba(120,190,230,.3) 45%,rgba(30,136,201,0) 70%)}
/* contact */
.touch{left:0;top:2300px;width:1200px;height:515px;background:linear-gradient(100deg,#ffffff 0%,#f4f6f9 45%,#dfe5ec 75%,#eef1f5 100%)}
.touch .sec-title{top:40px}
.touch .sec-rule{top:84px}
.form{left:289px;top:130px;width:621px;height:343px;background:var(--white)}
.field{position:absolute;border:1px solid #bdbdbd;font:500 11px var(--head);color:var(--ink);padding:15px 14px}
.submit{position:absolute;left:239px;top:262px;width:144px;height:46px;background:var(--blue);color:var(--white);font:600 16px var(--head);display:flex;align-items:center;justify-content:center}
/* footer */
.footer{left:0;top:2815px;width:1200px;height:342px;background:var(--footer);color:var(--white)}
.footer h5{font:600 13px var(--head);letter-spacing:.5px}
.footer .links{font:400 12px/20px var(--head);margin-top:16px}
.f-item{display:flex;gap:10px;align-items:flex-start;font:400 12px/15px var(--head);margin-top:0}
.f-ic{width:22px;height:22px;border-radius:50%;background:var(--white);flex:none;display:flex;align-items:center;justify-content:center}
.footer .rule{left:139px;top:259px;width:933px;height:1px;background:#3c3c3c}
.copy{left:0;top:300px;width:1200px;text-align:center;font:400 10px var(--head);color:#ddd}
</style>
</head>
<body>

<header class="abs site-header">
  <div class="abs brand" style="left:131px;top:20px"><span class="brand-dot"></span>KORVAL Works Pty Ltd.</div>
  <div class="abs follow">FOLLOW US <span class="social-dot" style="background:#3b5998"></span><span class="social-dot" style="background:#1da1f2"></span><span class="social-dot" style="background:#1a2a5a"></span></div>
  <div class="abs callus">
    <svg width="26" height="26" viewBox="0 0 24 24" fill="none" stroke="#1e88c9" stroke-width="1.6"><path d="M5 3h4l2 5-2.5 1.5a11 11 0 0 0 6 6L16 13l5 2v4a2 2 0 0 1-2 2A16 16 0 0 1 3 5a2 2 0 0 1 2-2z"/></svg>
    <div><small>CALL US</small><strong>888.888.8888</strong></div>
  </div>
  <nav class="abs nav"><span class="active">HOME</span><span>ABOUT US</span><span>SERVICES</span><span>TESTIMONIALS</span><span>BLOG</span><span>CONTACT US</span></nav>
</header>

<section class="abs hero" role="img" aria-label="Dusk photo of a large lit villa beside a swimming pool">
  <h1 class="abs">COMPLETE<br>PACKAGE<br>SOLUTIONS</h1>
  <p class="abs">Electrical, Audio Visual<br>and Data services</p>
  <div class="abs btn-green">READ MORE</div>
  <div class="abs dots"><i></i><i></i><i class="on"></i><i></i><i></i></div>
</section>

<h2 class="abs sec-title" style="top:705px">OUR SERVICES</h2>
<div class="abs sec-rule" style="top:749px"></div>

<article class="abs card" style="left:131px;top:794px">
  <div class="photo" role="img" aria-label="Electrician testing a switchboard with a multimeter" style="background:linear-gradient(135deg,#c9ccd2,#e6e8eb 50%,#c2603a 80%,#9aa0a8)"></div>
  <div class="badge"><svg width="30" height="34" viewBox="0 0 30 34" fill="none" stroke="#1e88c9" stroke-width="3"><path d="M10 2v8M20 2v8M6 10h18v6a9 9 0 0 1-18 0z"/><path d="M15 25v5"/></svg></div>
  <h3>ELECTRICAL</h3>
  <p>Lorem ipsum dolor sit amet, consectetur adipiscing elit, sed do eiusmod tempor incididunt ut labore et dolore.</p>
  <div class="btn-green">READ MORE</div>
</article>

<article class="abs card" style="left:455px;top:794px">
  <div class="photo" role="img" aria-label="Conference microphones on a boardroom table" style="background:linear-gradient(180deg,#e9ecef,#cfd3d8 55%,#8b6e57 80%,#b89a80)"></div>
  <div class="badge" style="background:var(--blue)"><svg width="32" height="32" viewBox="0 0 32 32" fill="none" stroke="#fff" stroke-width="3"><circle cx="21" cy="10" r="6"/><path d="M16 15 5 27"/></svg></div>
  <h3 style="margin-top:36px">AUDIO VISUAL</h3>
  <p>Lorem ipsum dolor sit amet, consectetur adipiscing elit, sed do eiusmod tempor incididunt ut labore et dolore.</p>
  <div class="btn-green">READ MORE</div>
</article>

<article class="abs card" style="left:780px;top:794px">
  <div class="photo" role="img" aria-label="Network switch with blue and yellow patch cables" style="background:linear-gradient(160deg,#1c3f9a,#2a66d0 45%,#d9c338 75%,#1b2f6e)"></div>
  <div class="badge"><svg width="28" height="32" viewBox="0 0 28 32" fill="#1e88c9"><rect x="6" y="14" width="16" height="16" rx="2"/><rect x="8" y="2" width="2" height="9"/><rect x="13" y="2" width="2" height="9"/><rect x="18" y="2" width="2" height="9"/></svg></div>
  <h3 style="margin-top:36px">DATA AND SUSTAINABLE PRACTICES</h3>
  <p>Lorem ipsum dolor sit amet, consectetur adipiscing elit, sed do eiusmod tempor incididunt ut labore et dolore.</p>
  <div class="btn-green">READ MORE</div>
</article>

<section class="abs welcome">
  <div class="abs photo" role="img" aria-label="Technician in blue overalls operating switchgear panels"></div>
  <h2 class="abs">WELCOME TO<span>KORVAL WORKS</span></h2>
  <div class="abs rule"></div>
  <p class="abs">Sed ut perspiciatis unde omnis iste natus error sit voluptatem accusantium doloremque laudantium, totam rem aperiam, eaque ipsa quae ab illo inventore veritatis et quasi architecto beatae vitae dicta sunt explicabo. Nemo enim ipsam voluptatem quia voluptas sit aspernatur aut odit aut fugit, sed quia consequuntur magni dolores eos qui ratione voluptatem sequi nesciunt. Neque porro quisquam est, qui dolorem ipsum quia dolor sit amet, consectetur, adipisci velit, sed quia non numquam eius modi tempora incidunt ut labore et .</p>
  <div class="abs btn-green">READ MORE</div>
</section>

<section class="abs why">
  <h2 class="abs sec-title">WHY CHOOSE US</h2>
  <div class="abs sec-rule"></div>
  <div class="abs emblem" role="img" aria-label="Faint brand emblem decoration"></div>

  <div class="abs feat-icon" style="left:129px;top:173px"><svg width="44" height="44" viewBox="0 0 24 24" fill="#1e88c9"><circle cx="12" cy="12" r="9"/><circle cx="12" cy="10" r="3" fill="#fff"/><path d="M6.5 17a6 6 0 0 1 11 0" fill="#fff"/></svg></div>
  <div class="abs feat" style="left:230px;top:165px"><h4>PROFESSIONALISM</h4><p>Sed ut perspiciatis unde omnis iste natus error sit voluptatem accusantium doloremque laudantium, totam.</p></div>
  <div class="abs divider" style="left:131px;top:305px;width:274px"></div>
  <div class="abs feat-icon" style="left:129px;top:350px"><svg width="44" height="44" viewBox="0 0 24 24" fill="none" stroke="#1e88c9" stroke-width="2"><circle cx="12" cy="12" r="9"/><path d="m8 12 3 3 5-6"/></svg></div>
  <div class="abs feat" style="left:230px;top:342px"><h4>WARRANTY GUARANTEED ON WORKMANSHIP</h4><p>Sed ut perspiciatis unde omnis iste natus error sit voluptatem accusantium doloremque laudantium, totam.</p></div>

  <div class="abs feat-icon" style="left:991px;top:173px"><svg width="44" height="44" viewBox="0 0 24 24" fill="none" stroke="#1e88c9" stroke-width="2"><circle cx="12" cy="12" r="8"/><path d="M12 8v4l3 2"/></svg></div>
  <div class="abs feat" style="left:750px;top:165px;text-align:left;width:205px;left:795px"><h4>LONG TERM CLIENTELE</h4><p>Sed ut perspiciatis unde omnis iste natus error sit voluptatem accusantium doloremque laudantium, totam.</p></div>
  <div class="abs divider" style="left:795px;top:305px;width:272px"></div>
  <div class="abs feat-icon" style="left:991px;top:350px"><svg width="44" height="44" viewBox="0 0 24 24" fill="none" stroke="#1e88c9" stroke-width="2"><circle cx="14" cy="7" r="4"/><path d="M3 18l4-3h6l4-2M3 21h9l8-5"/></svg></div>
  <div class="abs feat" style="left:795px;top:342px"><h4>SUSTAINABLE PRACTICES</h4><p>Sed ut perspiciatis unde omnis iste natus error sit voluptatem accusantium doloremque laudantium, totam.</p></div>
</section>

<section class="abs touch" role="img" aria-label="Faint background photo of a technician at work">
  <h2 class="abs sec-title">GET IN TOUCH</h2>
  <div class="abs sec-rule"></div>
  <form class="abs form">
    <div class="field" style="left:39px;top:35px;width:263px;height:42px">NAME</div>
    <div class="field" style="left:316px;top:35px;width:263px;height:42px">E MAIL</div>
    <div class="field" style="left:39px;top:90px;width:263px;height:42px">PHONE</div>
    <div class="field" style="left:316px;top:90px;width:263px;height:42px">SUBJECT</div>
    <div class="field" style="left:39px;top:145px;width:540px;height:91px">MESSAGE</div>
    <div class="submit">SUBMIT</div>
  </form>
</section>

<footer class="abs footer">
  <div class="abs brand" style="left:131px;top:92px"><span class="brand-dot"></span>KORVAL Works Pty Ltd.</div>
  <div class="abs" style="left:518px;top:42px"><h5>MENU</h5>
    <div class="links">HOME<br>ABOUT US<br>SERVICES<br>TESTIMONIALS<br>BLOG<br>CONTACT US</div></div>
  <div class="abs" style="left:706px;top:42px"><h5>CONTACT US</h5>
    <div class="f-item" style="margin-top:20px"><span class="f-ic"><svg width="10" height="12" viewBox="0 0 10 12" fill="#222"><path d="M5 0a4 4 0 0 1 4 4c0 3-4 8-4 8S1 7 1 4a4 4 0 0 1 4-4z"/></svg></span>5120 Harlow Street<br>Belmont, VIC 3216</div>
    <div class="f-item" style="margin-top:20px"><span class="f-ic"><svg width="11" height="11" viewBox="0 0 24 24" fill="#222"><path d="M5 3h4l2 5-2.5 1.5a11 11 0 0 0 6 6L16 13l5 2v4a2 2 0 0 1-2 2A16 16 0 0 1 3 5a2 2 0 0 1 2-2z"/></svg></span>Call Us<br>888.888.8888</div>
    <div class="f-item" style="margin-top:20px"><span class="f-ic"><svg width="11" height="9" viewBox="0 0 11 9" fill="#222"><rect width="11" height="9" rx="1"/><path d="M0 1l5.5 4L11 1" stroke="#fff" fill="none"/></svg></span>E mail Us<br>Info@korvalworks.com.au</div>
  </div>
  <div class="abs" style="left:968px;top:42px"><h5>FOLLOW US</h5>
    <div class="f-item" style="margin-top:20px;margin-left:10px"><span class="f-ic"></span>Like us on<br>SOCIALHUB</div>
    <div class="f-item" style="margin-top:20px;margin-left:10px"><span class="f-ic"></span>Follow us on<br>CHIRPLINE</div>
    <div class="f-item" style="margin-top:20px;margin-left:10px"><span class="f-ic"></span>Follow us on<br>PROLINK</div>
  </div>
  <div class="abs rule"></div>
  <div class="abs copy">Copyright © 2020 All Rights Reserved</div>
</footer>

</body>
</html>
```